Flyer Design Project for a Seminar "Charting The Handover"

KTMW Chartered Accountants would like a flyer invitation designed for our upcoming seminar "Charting The Handover." The invitation should be created in MS Word, for editing capabilities on our end.

Seminar Title: "Charting The Handover: Securing and Growing Worth Across An Ownership Shift"

This is a complimentary breakfast seminar for Owners and CEOs of private corporations with revenues ranging from $2M to $150M.

Please leave substantial room to enter overview information on the seminar and topics of discussion.

We are open to bold colours and interesting graphics.

An example of a very amateur in-house design is attached.

Target Market(s)

Business owners and CEOs (typically men between 40 and 50 years old)

Industry/Entity Type

Business

Requirements
Must have
• -Substantial space to enter overview info about the seminar
-Space to enter logistical info about the seminar (i.e When, Where and RSVP info)
-Text should be Gill Sans. 1 page only
Should not have
• Stock photos of fake office people or American dollars (we are a Canadian company)!

```html
<!DOCTYPE html>
<html lang="en">
<head>
<meta charset="utf-8">
<title>Charting The Handover – Complimentary Breakfast Seminar</title>
<link rel="stylesheet" href="https://fonts.googleapis.com/css2?family=Cabin:wght@400;600;700&family=Lato:wght@400;700&display=swap">
<style>
  :root {
    --teal: #1f7e8a;
    --teal-light: #4aa3ad;
    --teal-dark: #15646e;
    --ink: #1d1d1d;
    --red: #c4161c;
    --rule: #9aa3a6;
    --navy: #1e2f52;
    --paper: #ffffff;
  }
  * { box-sizing: border-box; margin: 0; padding: 0; }
  html, body { width: 813px; height: 1200px; overflow: hidden; background: var(--paper); }
  body { font-family: "Lato", Arial, sans-serif; color: var(--ink); }
  .flyer { position: relative; width: 813px; height: 1200px; overflow: hidden; }

  .eyebrow-band {
    height: 40px; margin-top: 4px;
    background: linear-gradient(90deg, var(--teal-dark), var(--teal-light) 70%, #cfe6e9);
    color: #fff; font-family: "Cabin", sans-serif; font-weight: 700;
    font-size: 19px; letter-spacing: 0.5px; text-transform: uppercase;
    padding: 10px 20px 0;
  }
  .title-band {
    height: 96px;
    background: linear-gradient(90deg, var(--teal), var(--teal-light) 75%, #d6eaec);
    border-top: 2px solid #fff;
    padding: 22px 20px 0;
  }
  .title-band h1 {
    color: #fff; font-family: "Cabin", sans-serif; font-weight: 600;
    font-size: 50px; line-height: 1;
  }
  .subtitle {
    color: var(--teal); font-family: "Cabin", sans-serif; font-weight: 700;
    font-size: 25px; line-height: 1.25; padding: 16px 20px 0; width: 760px;
  }

  .logistics {
    display: grid; grid-template-columns: 210px 260px 1fr;
    margin: 22px 20px 0; column-gap: 10px;
  }
  .logistics h2 {
    color: var(--teal); font-family: "Cabin", sans-serif; font-weight: 700;
    font-size: 22px; border-bottom: 1px solid var(--rule); padding-bottom: 4px; margin-bottom: 8px;
  }
  .logistics p { font-size: 15px; line-height: 1.35; }

  .notice { color: var(--red); font-weight: 700; font-size: 16px; margin: 18px 20px 0; }
  .audience {
    color: var(--teal-dark); font-family: "Cabin", sans-serif; font-size: 21px;
    line-height: 1.3; margin: 14px 20px 0; width: 770px;
  }

  .overview {
    position: absolute; left: 15px; top: 492px; width: 783px; height: 590px;
    border: 1px solid var(--rule); padding: 26px 30px;
    font-size: 15.5px; line-height: 1.45;
  }
  .overview p { margin-bottom: 18px; }
  .overview .topics-heading { font-weight: 700; margin-bottom: 8px; }
  .overview ul { margin: 0 0 20px 38px; }
  .overview li { margin-bottom: 12px; }

  .sponsors {
    position: absolute; left: 20px; right: 20px; top: 1100px; height: 86px;
    display: flex; justify-content: space-between; align-items: center;
  }
  .sponsor { display: flex; align-items: center; gap: 10px; font-family: "Cabin", sans-serif; font-weight: 700; }
  .sponsor-host { color: var(--navy); font-size: 34px; }
  .sponsor-host .mark { width: 30px; height: 30px; background: var(--navy); }
  .sponsor-partner { color: var(--teal); font-size: 19px; text-transform: uppercase; letter-spacing: 1px; text-align: right; line-height: 1.2; }
</style>
</head>
<body>
<main class="flyer">
  <header>
    <div class="eyebrow-band">Complimentary Breakfast Seminar</div>
    <div class="title-band"><h1>Charting The Handover</h1></div>
    <p class="subtitle">Securing and Growing Worth Across An Ownership Shift</p>
  </header>

  <section class="logistics">
    <div class="logistics-when">
      <h2>When</h2>
      <p>Thursday,<br>February 24, 2011<br>7:45 - 10:00 AM</p>
    </div>
    <div class="logistics-where">
      <h2>Where</h2>
      <p>KTMW Chartered<br>Accountants<br>1180 Harbourview Road, Ste 300<br>Toronto</p>
    </div>
    <div class="logistics-rsvp">
      <h2>RSVP</h2>
      <p>Claire Dunmore<br>416.555.0148 x 210<br>events@ktmw.ca</p>
    </div>
  </section>

  <p class="notice">Pre-registration is required for attendance.</p>
  <p class="audience">A complimentary breakfast seminar for Owners and CEOs of private corporations with revenues ranging from $2 Million to $150 Million.</p>

  <section class="overview">
    <p>Almost two-thirds of independent business owners in Canada are planning to exit their business within the next decade. The spoils will go to those who have planned in advance. Are you one of them?</p>
    <p>Join Martin Ellery, Partner at KTMW Chartered Accountants, and Owen Radcliffe, Co-Founder of Northvale Capital Partners, for a compelling overview of one of the most critical issues affecting privately-held businesses today.</p>
    <p class="topics-heading">Topics of discussion will include:</p>
    <ul>
      <li>The alternatives for exiting a business and the implications of each</li>
      <li>Tax minimization strategies for the sale/transfer of your business</li>
      <li>Tactics for gaining control of the deal to achieve a successful sale and maximize the value you receive from it</li>
      <li>Real-life case studies and lessons to be learned from them</li>
    </ul>
    <p>All attendees will receive detailed seminar handouts and a complimentary consultation with both Martin and Owen to map out the next steps in developing an effective exit plan for their business.</p>
  </section>

  <footer class="sponsors">
    <div class="sponsor sponsor-host"><span class="mark"></span>KTMW</div>
    <div class="sponsor sponsor-partner">Northvale<br>Capital Partners</div>
  </footer>
</main>
</body>
</html>
```